Olive Oil Label Needs Graphic Designs

We need two sister label designs for 500ml bottles for our new brand "Casa Lumen". Casa Lumen is a high-end olive oil from Baeza, Spain which will be sold in the US. The oil will be produced from both Arbequina olives and Picual olives. Therefore, envisioning the same design just a different color scheme for the different labels.
The label should have the following characteristics; clean and simple, stand-out from mainstream labels, be eye-catching, give perception of high-end / high-quality.
Our current thinking of what we want (but please let your creative juices flow); lighter background, to be more eye catching, graphics of and olive, a olive branch or olive tree.
Text which should appear on the label are (not necessarily in this order);
Casa Lumen
Extra Virgin Olive Oil
Family Reserve
Arbequina (One design)
Picual (Second design)
The label should be about 3 inches wide and 5.5 inches in height.

```html
<!DOCTYPE html>
<html lang="en">
<head>
<meta charset="utf-8">
<title>Casa Lumen – Family Reserve Labels</title>
<link rel="stylesheet" href="https://fonts.googleapis.com/css2?family=Fondamento&family=Libre+Caslon+Text:wght@400;700&display=swap">
<style>
  :root {
    --page: #ffffff;
    --band: #5b1420;
    --band-text: #f4e9b8;
    --cream: #f7eeb8;
    --ink: #3f3a12;
    --brand: #5f6a1c;
    --rule: #6e6420;
    --picual-body: #7e1b20;
    --picual-text: #f4e9b8;
    --picual-variety: #6b1418;
    --arbequina-body: #b59d3a;
    --arbequina-text: #3a2a08;
    --arbequina-variety: #4d4210;
    --tree: #8a8a4a;
    --sprig: #7d8a3a;
  }
  * { box-sizing: border-box; margin: 0; padding: 0; }
  html, body {
    width: 884px; height: 1200px; overflow: hidden;
    background: var(--page);
  }
  .canvas {
    position: relative; width: 884px; height: 1200px;
    display: flex; justify-content: center; align-items: center; gap: 44px;
  }
  .label {
    --body: var(--picual-body);
    --body-text: var(--picual-text);
    --variety: var(--picual-variety);
    width: 380px; height: 548px;
    background: var(--body);
    border-radius: 20px 20px 34px 34px;
    overflow: hidden;
    display: flex; flex-direction: column; align-items: center;
    box-shadow: inset 0 0 0 2px rgba(0,0,0,0.12);
  }
  .label--arbequina {
    --body: var(--arbequina-body);
    --body-text: var(--arbequina-text);
    --variety: var(--arbequina-variety);
  }
  .label__band {
    width: 100%; height: 48px;
    background: var(--band);
    display: flex; align-items: center; justify-content: center;
    font-family: "Libre Caslon Text", Georgia, serif;
    font-size: 25px; letter-spacing: 0.5px;
    color: var(--band-text);
  }
  .cartouche {
    position: relative;
    margin-top: 22px;
    width: 318px; height: 272px;
  }
  .cartouche__frame { position: absolute; inset: 0; }
  .cartouche__content {
    position: absolute; inset: 0;
    display: flex; flex-direction: column; align-items: center;
    padding-top: 18px;
  }
  .tree-art {
    width: 84px; height: 56px;
    border-radius: 50% 50% 10px 10px;
    background: radial-gradient(ellipse at 50% 40%, var(--tree), #6f7038);
  }
  .rule {
    width: 220px; height: 0;
    border-top: 1.5px solid var(--rule);
  }
  .rule--top { margin-top: 6px; }
  .brand-name {
    font-family: "Fondamento", Georgia, cursive;
    font-size: 46px; line-height: 1;
    color: var(--brand);
    margin: 6px 0 8px;
  }
  .variety {
    font-family: "Fondamento", Georgia, cursive;
    font-size: 36px; line-height: 1;
    color: var(--variety);
    margin-top: 8px;
  }
  .sprig-art {
    margin-top: 8px;
    width: 76px; height: 28px;
    border-radius: 50%;
    background: linear-gradient(90deg, #5f6d2a, var(--sprig), #8f2a2a);
  }
  .label__product {
    margin-top: 32px;
    font-family: "Libre Caslon Text", Georgia, serif;
    font-size: 25px;
    color: var(--body-text);
  }
  .label__volume {
    margin-top: 12px;
    font-family: "Libre Caslon Text", Georgia, serif;
    font-weight: 700; font-size: 22px; letter-spacing: 1px;
    color: var(--body-text);
  }
  .label__volume small { font-size: 15px; }
</style>
</head>
<body>
<main class="canvas">

  <section class="label label--picual">
    <header class="label__band">FAMILY RESERVE</header>
    <div class="cartouche">
      <svg class="cartouche__frame" viewBox="0 0 318 272" aria-hidden="true">
        <path d="M40 6 H278 Q282 22 300 24 Q312 26 312 40 V232 Q312 246 300 248 Q282 250 278 266 H40 Q36 250 18 248 Q6 246 6 232 V40 Q6 26 18 24 Q36 22 40 6 Z"
              fill="var(--cream)" stroke="#3a2a10" stroke-width="3"/>
        <path d="M46 14 H272 Q276 28 292 31 Q304 33 304 44 V228 Q304 239 292 241 Q276 244 272 258 H46 Q42 244 26 241 Q14 239 14 228 V44 Q14 33 26 31 Q42 28 46 14 Z"
              fill="none" stroke="#8a7a30" stroke-width="1.2"/>
      </svg>
      <div class="cartouche__content">
        <div class="tree-art" role="img" aria-label="Olive tree illustration"></div>
        <div class="rule rule--top"></div>
        <div class="brand-name">Casa Lumen</div>
        <div class="rule"></div>
        <div class="variety">Picual</div>
        <div class="sprig-art" role="img" aria-label="Olive sprig with leaves and olives"></div>
      </div>
    </div>
    <p class="label__product">Extra Virgin Olive Oil</p>
    <p class="label__volume">500 <small>ML</small></p>
  </section>

  <section class="label label--arbequina">
    <header class="label__band">FAMILY RESERVE</header>
    <div class="cartouche">
      <svg class="cartouche__frame" viewBox="0 0 318 272" aria-hidden="true">
        <path d="M40 6 H278 Q282 22 300 24 Q312 26 312 40 V232 Q312 246 300 248 Q282 250 278 266 H40 Q36 250 18 248 Q6 246 6 232 V40 Q6 26 18 24 Q36 22 40 6 Z"
              fill="var(--cream)" stroke="#3a2a10" stroke-width="3"/>
        <path d="M46 14 H272 Q276 28 292 31 Q304 33 304 44 V228 Q304 239 292 241 Q276 244 272 258 H46 Q42 244 26 241 Q14 239 14 228 V44 Q14 33 26 31 Q42 28 46 14 Z"
              fill="none" stroke="#8a7a30" stroke-width="1.2"/>
      </svg>
      <div class="cartouche__content">
        <div class="tree-art" role="img" aria-label="Olive tree illustration"></div>
        <div class="rule rule--top"></div>
        <div class="brand-name">Casa Lumen</div>
        <div class="rule"></div>
        <div class="variety">Arbequina</div>
        <div class="sprig-art" role="img" aria-label="Olive sprig with leaves and olives"></div>
      </div>
    </div>
    <p class="label__product">Extra Virgin Olive Oil</p>
    <p class="label__volume">500 <small>ML</small></p>
  </section>

</main>
</body>
</html>
```